Brisk Lyceum Website

We are looking for a new design of our website. The current website is www.brisklyceum-example.com. The company is the #1 pre-college math and science program in Orange County, CA. We would like to see designs that integrate our logo with a modern color scheme. We are also open for suggestions that could improve our logo. We would like a simple, minimal, clean, classy, and vibrant front-page user interface design that give the premium, modern, innovative, creative, and premier brand feel. We like the "New Retro Colors for the Web" as described here: http://www.pixelharbor-example.net/en/layout-notes-2013/.

Target Market(s)

The target market is parents with K-12 students from a diverse population. Parents are well educated with family income > $150,000. Most of the decision makers are mothers from immigrate families: 30% Chinese, 30% Korean, 15% Indian, 24% White.

Industry/Entity Type

College

Requirements
Must have
• Must read our statement of differentiation at:
• http://brisklyceum-example.com/about-us
• Your design must be reflective of your understanding of the statements.
Nice to have
• The design should also be mobil friendly.
Should not have
• While most of our current classes are math, our company is expanding to include STEM (Science, Technology, Engineering, and Math) for gifted students. Therefore, the site should not be JUST a math education site.

```html
<!DOCTYPE html>
<html lang="en">
<head>
<meta charset="utf-8">
<title>Brisk Lyceum for Gifted Youth</title>
<link rel="stylesheet" href="https://fonts.googleapis.com/css2?family=Mulish:wght@300;400&family=Open+Sans:wght@400;600&display=swap">
<style>
  :root {
    --navy: #0b4a74;
    --navy-dark: #083d61;
    --sky: #6ec7f0;
    --sky-soft: #8ed3f4;
    --green: #5fb336;
    --green-dark: #3f8f1f;
    --paper: #efefef;
    --white: #ffffff;
    --ink: #2a2a2a;
    --muted: #8c8c8c;
    --rule: #d8d8d8;
  }
  * { box-sizing: border-box; margin: 0; padding: 0; }
  html, body { width: 814px; height: 1200px; overflow: hidden; }
  body {
    position: relative;
    background: var(--white);
    font-family: "Open Sans", Arial, sans-serif;
    color: var(--ink);
  }
  .abs { position: absolute; }

  /* backgrounds */
  .top-band { left: 0; top: 0; width: 814px; height: 38px; background: var(--navy); }
  .paper-top { left: 0; top: 38px; width: 814px; height: 131px; background: var(--paper); }
  .paper-mid { left: 0; top: 383px; width: 814px; height: 372px; background: var(--paper); }

  /* navigation */
  .nav {
    left: 80px; top: 16px; width: 655px; height: 34px;
    background: var(--white); border-radius: 3px;
    box-shadow: 0 1px 3px rgba(0,0,0,.25);
  }
  .nav-item {
    position: absolute; top: 0; height: 34px; line-height: 34px;
    font-size: 7.5px; color: #555; letter-spacing: .2px; text-transform: uppercase;
  }
  .nav-item.active {
    top: 5px; left: 6px; width: 59px; height: 25px; line-height: 25px;
    background: linear-gradient(#72c44a, var(--green)); color: var(--white);
    text-align: center; border-radius: 2px;
  }
  .search {
    position: absolute; left: 529px; top: 5px; width: 120px; height: 23px;
    background: #eeeeee; border-radius: 2px; border: 1px solid #ddd;
  }
  .search span { position: absolute; left: 10px; top: 4px; font-size: 8px; color: #333; }
  .search .divider { position: absolute; left: 96px; top: 2px; width: 1px; height: 17px; background: #cfcfcf; }
  .search svg { position: absolute; left: 101px; top: 3px; }

  /* brand */
  .brand { left: 0; top: 68px; width: 814px; display: flex; justify-content: center; align-items: center; gap: 10px; }
  .brand-dot { width: 34px; height: 34px; border-radius: 50%; background: var(--green); }
  .brand-name { font-family: "Mulish", sans-serif; font-weight: 400; font-size: 27px; color: var(--navy); }

  /* slider */
  .slider {
    left: 80px; top: 128px; width: 655px; height: 292px; background: var(--white);
    border-radius: 3px; box-shadow: 0 2px 6px rgba(0,0,0,.2);
  }
  .slide-photo {
    position: absolute; left: 8px; top: 8px; width: 637px; height: 276px;
    background: linear-gradient(180deg, #4f7a3a 0%, #7a9b63 40%, #5a6f8f 75%, #6c9a48 100%);
  }
  .slider svg { position: absolute; top: 124px; }

  /* subject cards */
  .card {
    top: 458px; width: 153px; height: 256px; background: var(--white);
    border-radius: 3px; box-shadow: 0 0 2px rgba(0,0,0,.15); text-align: center;
  }
  .card-title {
    height: 42px; line-height: 42px; font-family: "Mulish", sans-serif; font-size: 19px;
    color: var(--white); border-radius: 3px 3px 0 0;
  }
  .card.navy .card-title { background: var(--navy); }
  .card.sky .card-title { background: var(--sky-soft); }
  .card-photo { width: 132px; height: 62px; margin: 12px auto 0; }
  .card-text { margin: 10px 8px 0; font-size: 9px; line-height: 11.3px; color: var(--muted); }
  .btn {
    display: block; width: 80px; height: 22px; line-height: 22px; margin: 9px auto 0;
    background: linear-gradient(#6cc23f, var(--green-dark)); color: var(--white);
    font-size: 8.5px; border-radius: 2px; box-shadow: 0 1px 2px rgba(0,0,0,.35);
  }

  /* welcome */
  .welcome-photo {
    left: 80px; top: 785px; width: 148px; height: 147px;
    background: linear-gradient(180deg, #9fb3c7 0%, #6d7f95 45%, #3b3b45 100%);
  }
  .welcome-title {
    left: 247px; top: 778px; width: 260px; font-family: "Mulish", sans-serif; font-weight: 300;
    font-size: 25px; line-height: 30.5px; color: #111;
  }
  .welcome-lead {
    left: 247px; top: 879px; width: 250px; font-size: 8.7px; line-height: 13.7px;
    color: var(--navy); text-transform: uppercase;
  }
  .welcome-body { left: 79px; top: 943px; width: 420px; font-size: 8.7px; line-height: 13.5px; color: #222; }
  .features { left: 79px; top: 987px; width: 420px; list-style: none; }
  .feature { position: relative; padding-left: 39px; font-size: 8.7px; line-height: 13.5px; color: #222; }
  .feature .tick {
    position: absolute; left: 1px; top: 0; width: 18px; height: 18px; border-radius: 50%;
    background: var(--green);
  }
  .feature .tick svg { position: absolute; left: 6px; top: 5px; }

  /* news */
  .news-title { left: 524px; top: 778px; font-family: "Mulish", sans-serif; font-size: 19px; color: var(--navy); }
  .news-rule { left: 524px; top: 808px; width: 210px; height: 1px; background: var(--rule); }
  .news-item { left: 524px; width: 210px; height: 76px; }
  .date {
    position: absolute; left: 0; top: 0; width: 44px; height: 73px;
    background: var(--sky); color: var(--white); text-align: center;
  }
  .date .day { display: block; font-family: "Mulish", sans-serif; font-size: 23px; line-height: 28px; margin-top: 1px; }
  .date .month { display: block; font-size: 10px; line-height: 12px; }
  .date .bar { position: absolute; left: 0; bottom: 0; width: 44px; height: 19px; background: #8dd3f3; border-top: 1px solid var(--white); }
  .date .bar svg { position: absolute; left: 16px; top: 5px; }
  .date::after {
    content: ""; position: absolute; right: -7px; top: 11px;
    border-left: 7px solid var(--sky); border-top: 6px solid transparent; border-bottom: 6px solid transparent;
  }
  .news-heading { position: absolute; left: 61px; top: -3px; font-family: "Mulish", sans-serif; font-size: 16px; color: #111; }
  .news-text { position: absolute; left: 61px; top: 31px; width: 145px; font-size: 8.4px; line-height: 11.3px; color: var(--muted); }

  /* footer */
  .footer { left: 0; top: 1150px; width: 814px; height: 50px; background: var(--navy); }
  .footer-note { position: absolute; left: 83px; top: 17px; font-size: 10.5px; color: var(--white); }
  .footer-note em { font-style: normal; color: var(--sky); }
  .social { position: absolute; top: 14px; width: 20px; height: 20px; border-radius: 50%; background: #5a9cc8; }
</style>
</head>
<body>
  <div class="abs top-band"></div>
  <div class="abs paper-top"></div>
  <div class="abs paper-mid"></div>

  <nav class="abs nav">
    <span class="nav-item active">Home</span>
    <span class="nav-item" style="left:80px">About Us</span>
    <span class="nav-item" style="left:157px">Subjects</span>
    <span class="nav-item" style="left:234px">Science Fair</span>
    <span class="nav-item" style="left:328px">Fall 2013</span>
    <span class="nav-item" style="left:406px">Results</span>
    <span class="nav-item" style="left:474px">Contact</span>
    <div class="search">
      <span>Search</span>
      <div class="divider"></div>
      <svg width="15" height="15" viewBox="0 0 15 15"><circle cx="6" cy="6" r="4.3" fill="none" stroke="#555" stroke-width="1.6"/><line x1="9.2" y1="9.2" x2="13.5" y2="13.5" stroke="#555" stroke-width="2"/></svg>
    </div>
  </nav>

  <div class="abs brand">
    <div class="brand-dot"></div>
    <div class="brand-name">Brisk Lyceum</div>
  </div>

  <section class="abs slider">
    <div class="slide-photo" role="img" aria-label="Photo of four smiling students sitting on the grass with open notebooks"></div>
    <svg style="left:22px" width="22" height="44" viewBox="0 0 22 44"><polyline points="20,2 3,22 20,42" fill="none" stroke="#fff" stroke-width="1.5"/></svg>
    <svg style="left:612px" width="22" height="44" viewBox="0 0 22 44"><polyline points="2,2 19,22 2,42" fill="none" stroke="#fff" stroke-width="1.5"/></svg>
  </section>

  <article class="abs card navy" style="left:80px">
    <h2 class="card-title" style="font-weight:400">Math</h2>
    <div class="card-photo" role="img" aria-label="Photo of a student at a chalkboard covered in equations" style="background:linear-gradient(90deg,#2a2d2e,#3d4244,#26292a)"></div>
    <p class="card-text">Highly gifted students<br>who exhaust the above math<br>courses will be placed into<br>courses at local universities.<br>We also provide<br>road-maps for students with<br>exceptional talent</p>
    <span class="btn">DETAILS</span>
  </article>
  <article class="abs card sky" style="left:247px">
    <h2 class="card-title" style="font-weight:400">Physics</h2>
    <div class="card-photo" role="img" aria-label="Photo of a modern campus building under a blue sky" style="background:linear-gradient(180deg,#4f8fd6,#a9c9ea 55%,#b8a88a)"></div>
    <p class="card-text">Highly gifted students<br>who exhaust the above math<br>courses will be placed into<br>courses at local universities.<br>We also provide<br>road-maps for students with<br>exceptional talent</p>
    <span class="btn">DETAILS</span>
  </article>
  <article class="abs card navy" style="left:413px">
    <h2 class="card-title" style="font-weight:400">Chemistry</h2>
    <div class="card-photo" role="img" aria-label="Photo of laboratory flasks filled with coloured liquids" style="background:linear-gradient(180deg,#f2eee9,#d9d3cc 60%,#c8663a)"></div>
    <p class="card-text">Highly gifted students<br>who exhaust the above math<br>courses will be placed into<br>courses at local universities.<br>We also provide<br>road-maps for students with<br>exceptional talent</p>
    <span class="btn">DETAILS</span>
  </article>
  <article class="abs card sky" style="left:581px">
    <h2 class="card-title" style="font-weight:400">Biology</h2>
    <div class="card-photo" role="img" aria-label="Micrograph of green plant cells" style="background:radial-gradient(circle,#c8e832,#8cc820 60%,#5a8a3a)"></div>
    <p class="card-text">Highly gifted students<br>who exhaust the above math<br>courses will be placed into<br>courses at local universities.<br>We also provide<br>road-maps for students with<br>exceptional talent</p>
    <span class="btn">DETAILS</span>
  </article>

  <div class="abs welcome-photo" role="img" aria-label="Photo of a businesswoman offering a handshake in front of workers in various professions"></div>
  <h1 class="abs welcome-title" style="font-weight:300">Welcome to<br>Brisk Lyceum for<br>Gifted Youth</h1>
  <p class="abs welcome-lead">We provide after-school enrichment programs in math, physics, chemistry, biology, and computer science,mentor middle and high school science research projects.</p>
  <p class="abs welcome-body">and offer college counseling to aspiring students in pursuing their college dreams. Please explore this website to learn more about our programs and our approach to gifted education.</p>
  <ul class="abs features">
    <li class="feature" style="margin-top:0;padding-top:2px"><span class="tick"><svg width="6" height="8" viewBox="0 0 6 8"><polyline points="1,1 4.5,4 1,7" fill="none" stroke="#fff" stroke-width="1.4"/></svg></span>eLearning to access our Online Learning Management System for current students<br>and families.</li>
    <li class="feature" style="margin-top:18px;padding-top:2px"><span class="tick"><svg width="6" height="8" viewBox="0 0 6 8"><polyline points="1,1 4.5,4 1,7" fill="none" stroke="#fff" stroke-width="1.4"/></svg></span>Scheduler to make an appointment online for qualifying exams, gathering information, college counseling, or science research meetings.</li>
    <li class="feature" style="margin-top:17px;padding-top:2px"><span class="tick"><svg width="6" height="8" viewBox="0 0 6 8"><polyline points="1,1 4.5,4 1,7" fill="none" stroke="#fff" stroke-width="1.4"/></svg></span>Newsletter to subscribe to our monthly newsletter - The Brisk Learner.</li>
    <li class="feature" style="margin-top:12px;padding-top:2px"><span class="tick"><svg width="6" height="8" viewBox="0 0 6 8"><polyline points="1,1 4.5,4 1,7" fill="none" stroke="#fff" stroke-width="1.4"/></svg></span>Click on Registration to sign up for our classes.</li>
  </ul>

  <h2 class="abs news-title" style="font-weight:400">Latest News</h2>
  <div class="abs news-rule"></div>

  <article class="abs news-item" style="top:825px">
    <div class="date"><span class="day">29</span><span class="month">MAY</span><div class="bar"><svg width="12" height="9" viewBox="0 0 12 9"><ellipse cx="6" cy="4" rx="5.5" ry="3.6" fill="#fff"/><polygon points="3,6 2,9 6,7" fill="#fff"/></svg></div></div>
    <h3 class="news-heading" style="font-weight:400">News Heading</h3>
    <p class="news-text">The early registration deadline for returning.The early registration deadline for returning The early registration deadline .</p>
  </article>
  <article class="abs news-item" style="top:929px">
    <div class="date"><span class="day">02</span><span class="month">JUN</span><div class="bar"><svg width="12" height="9" viewBox="0 0 12 9"><ellipse cx="6" cy="4" rx="5.5" ry="3.6" fill="#fff"/><polygon points="3,6 2,9 6,7" fill="#fff"/></svg></div></div>
    <h3 class="news-heading" style="font-weight:400">News Heading</h3>
    <p class="news-text">The early registration deadline for returning.The early registration deadline for returning The early registration deadline .</p>
  </article>
  <article class="abs news-item" style="top:1037px">
    <div class="date"><span class="day">13</span><span class="month">JAN</span><div class="bar"><svg width="12" height="9" viewBox="0 0 12 9"><ellipse cx="6" cy="4" rx="5.5" ry="3.6" fill="#fff"/><polygon points="3,6 2,9 6,7" fill="#fff"/></svg></div></div>
    <h3 class="news-heading" style="font-weight:400">News Heading</h3>
    <p class="news-text">The early registration deadline for returning.The early registration deadline for returning The early registration deadline .</p>
  </article>

  <footer class="abs footer">
    <p class="footer-note"><em>Brisk Lyceum for Gifted Youth</em> © 2013 Privacy Policy</p>
    <span class="social" style="left:632px"></span>
    <span class="social" style="left:657px"></span>
    <span class="social" style="left:684px"></span>
    <span class="social" style="left:709px"></span>
  </footer>
</body>
</html>
```